TITLE: What Makes My Child’s Playing Talent Grow? SUB-TITLE: A Mother’s Plain Talk Manual for Coaching...

My book is for parents who have young children that are really into sports. My book empowers parents so they can motivate their children to succeed. It deals with sports psychology. Both my title and subtitle should be easy to read. Ideally, I would like a picture of young athlete(s) on the title. I have uploaded files of some books on Brindlemart that deal with the same subject. The last two files are 1) my company logo, please try to include these colors 2) an ebook cover I put together myself. You will notice an On-line bonus in the middle of the book, this Bonus needs to be on the cover.

Target Market(s)

Parents with children who play sports at a high level

Colors

Designer to choose colors to be used in the design.

Requirements
Must have
• Online Bonus feature as per my example.
• Dimensions: Pagelux = The ideal size of your eBook cover art is a height/width ratio of 1.6:1. This means that for every 1,000 pixels in width, the image should be 1,600 pixels in height.
Nice to have
• picture of a young athlete or young athletes

```html
<!DOCTYPE html>
<html lang="en">
<head>
<meta charset="utf-8">
<title>What Makes My Child’s Playing Talent Grow? — Book Cover</title>
<link rel="stylesheet" href="https://fonts.googleapis.com/css2?family=Montserrat:wght@400;600;700;800;900&family=Audiowide&display=swap">
<style>
  :root {
    --page: #ffffff;
    --navy-deep: #0f1a66;
    --navy: #1a2c96;
    --navy-band: #1b2466;
    --gold: #ffc21a;
    --amber: #f59a12;
    --badge: #f6a623;
    --badge-light: #fff6e6;
    --ink: #141414;
    --white: #ffffff;
    --sun: #fff4d8;
    --sky-warm: #efd3a4;
    --stand: #8f7f73;
    --skin-glow: #c98e68;
    --kit-teal: #4a9fb0;
    --kit-dark: #2b2c3f;
    --track: #5d7390;
  }
  * { margin: 0; padding: 0; box-sizing: border-box; }
  html, body { width: 1200px; height: 1200px; overflow: hidden; background: var(--page); }
  body { position: relative; font-family: "Montserrat", sans-serif; }

  .cover {
    position: absolute; left: 235px; top: 16px; width: 731px; height: 1168px;
    background:
      radial-gradient(ellipse at 30% 20%, rgba(60,90,200,.35), transparent 55%),
      radial-gradient(ellipse at 75% 45%, rgba(10,20,90,.5), transparent 60%),
      linear-gradient(180deg, var(--navy) 0%, var(--navy-deep) 45%, var(--navy) 60%);
    overflow: hidden;
  }

  .title { position: absolute; left: 0; right: 0; top: 92px; text-align: center; font-weight: 400; }
  .title-lead {
    display: block; color: var(--white); font-weight: 700; font-size: 44px; line-height: 54px;
  }
  .title-main {
    display: block; font-family: "Audiowide", "Montserrat", sans-serif;
    font-size: 56px; line-height: 68px; margin-top: 6px; text-transform: uppercase;
    background: linear-gradient(180deg, var(--gold) 35%, var(--amber) 90%);
    -webkit-background-clip: text; background-clip: text; color: transparent;
    filter: drop-shadow(0 3px 2px rgba(0,0,0,.7));
  }
  .title-end {
    display: block; font-family: "Montserrat", sans-serif; font-weight: 900;
    font-size: 54px; line-height: 62px; text-transform: uppercase;
    background: linear-gradient(180deg, var(--gold) 35%, var(--amber) 90%);
    -webkit-background-clip: text; background-clip: text; color: transparent;
    filter: drop-shadow(0 3px 2px rgba(0,0,0,.7));
  }
  .subtitle {
    position: absolute; left: 0; right: 0; top: 310px; text-align: center;
    color: var(--white); font-size: 17px; line-height: 24px; text-transform: uppercase;
  }

  .bonus-badge { position: absolute; left: 243px; top: 398px; width: 246px; height: 190px; z-index: 2; }

  .hero-photo {
    position: absolute; left: 0; top: 580px; width: 731px; height: 518px;
    background:
      linear-gradient(180deg, var(--navy-deep) 0%, rgba(15,26,102,.6) 6%, rgba(15,26,102,0) 16%),
      radial-gradient(circle at 86% 28%, var(--sun) 0%, rgba(255,244,216,.75) 12%, transparent 32%),
      radial-gradient(ellipse 60% 40% at 52% 66%, rgba(201,142,104,.85), transparent 70%),
      radial-gradient(ellipse 18% 30% at 82% 62%, rgba(74,159,176,.8), transparent 75%),
      radial-gradient(ellipse 20% 32% at 22% 64%, rgba(43,44,63,.75), transparent 75%),
      linear-gradient(180deg, var(--sky-warm) 14%, var(--sky-warm) 30%, var(--stand) 50%, var(--skin-glow) 64%, var(--track) 100%);
  }

  .author-band {
    position: absolute; left: 0; bottom: 0; width: 731px; height: 86px;
    background: var(--navy-band);
    display: flex; align-items: center; justify-content: center;
  }
  .author-name { color: var(--white); font-weight: 700; font-size: 22px; letter-spacing: .3px; }

  .brand-mark {
    position: absolute; left: 586px; top: 1020px; width: 112px; height: 112px;
    border-radius: 50%; background: var(--badge); border: 3px solid var(--white);
    display: flex; flex-direction: column; align-items: center; justify-content: center;
    color: var(--white); font-weight: 700; text-align: center; z-index: 2;
  }
  .brand-name { font-size: 15px; line-height: 18px; }
  .brand-site { font-size: 10px; margin-top: 4px; }
</style>
</head>
<body>
  <main class="cover">
    <h1 class="title">
      <span class="title-lead">What Makes My Child’s</span>
      <span class="title-main">Playing Talent</span>
      <span class="title-end">Grow?</span>
    </h1>
    <p class="subtitle">A Mother’s Plain Talk Manual for Coaching Confident,<br>Focused and Resilient Athletes</p>

    <svg class="bonus-badge" viewBox="0 0 246 190" aria-label="Free online workshop, $170 value, details inside">
      <g transform="translate(3 -5)">
        <polygon fill="var(--badge)" points="120,8 131,28 148,12 154,34 174,23 174,46 196,41 190,63 212,63 200,82 221,88 204,103 221,117 200,124 212,143 190,144 196,165 174,160 174,183 154,172 148,194 131,178 120,198 109,178 92,194 86,172 66,183 66,160 44,165 50,144 28,143 40,124 19,117 36,103 19,88 40,82 28,63 50,63 44,41 66,46 66,23 86,34 92,12 109,28" transform="translate(12 6) scale(.9)"/>
        <circle cx="120" cy="100" r="62" fill="var(--badge-light)"/>
        <circle cx="120" cy="100" r="56" fill="none" stroke="var(--badge)" stroke-width="2" stroke-dasharray="2 3"/>
        <g transform="rotate(-10 120 100)" font-family="Montserrat, sans-serif" font-weight="800" fill="var(--ink)" text-anchor="middle">
          <text x="120" y="76" font-size="15">$170 VALUE</text>
          <text x="120" y="91" font-size="10" font-weight="600">DETAILS INSIDE</text>
          <rect x="-2" y="102" width="244" height="32" fill="var(--badge)" stroke="var(--badge-light)" stroke-width="1.5"/>
          <text x="120" y="124" font-size="16">FREE ONLINE WORKSHOP</text>
        </g>
      </g>
    </svg>

    <div class="hero-photo" role="img" aria-label="Photo of four smiling young track athletes wearing medals, arms around each other on a sunlit stadium track"></div>

    <footer class="author-band"><span class="author-name">RAFE DONNELLY</span></footer>

    <div class="brand-mark">
      <span class="brand-name">Inner Play</span>
      <span class="brand-site">coachrafe.net</span>
    </div>
  </main>
</body>
</html>
```